Webpages for Sammalkivi Software Consulting

Needed: Webpage design.
Details:
One page site with good looking fonts and simple modern design. Logo would also be nice.
Page is for Software consulting company called: "Sammalkivi Software Consulting". Sammalkivi is my surname.
Pages should tell viewer that the company is reliable and its employees are hard-core professionals.
Company currently has one employee, that's me. So what I do is what this company does. I am software consultant. Basicly that means that I do Kahvi/JavaEE/Web programming as subcontractor.
Here is more detail information about me.
SPECIALTIES
- Enterprise Kernel EE Application Programming and Architectures,
- Web development and
- Agile development.
I have over a decade of experience on designing and creating Kahvi based web-services and applications to multiple interfaces. I also have plenty of experience about software architectures, design patterns and integration into third party systems. I’ve got good knowledge about agile software development and testing processes and I am experienced ScrumMaster and software project leader.
Target Market(s)
IT Businesses, Coding companies... Anyone who is buying coding as service.
Industry/Entity Type
Software

```html
<!DOCTYPE html>
<html lang="en">
<head>
<meta charset="utf-8">
<title>Sammalkivi Software Consulting</title>
<link rel="stylesheet" href="https://fonts.googleapis.com/css2?family=Gelasio:wght@700&family=Noto+Sans:wght@400&family=PT+Sans:wght@700&display=swap">
<style>
:root{
  --page:#f0f0f1;
  --white:#ffffff;
  --nav:#6b6b6b;
  --mid:#666666;
  --dark:#333333;
  --logo:#6e6e6e;
  --text:#111111;
  --muted:#333333;
  --strip-light:#e2e2e2;
  --strip-mid:#8c8c8c;
  --panel:#ececec;
  --tick:#4a0a10;
}
*{margin:0;padding:0;box-sizing:border-box}
html,body{width:1162px;height:1200px;overflow:hidden}
body{position:relative;background:var(--white);font-family:"Noto Sans",sans-serif;color:var(--text)}
.abs{position:absolute}
.header-band{left:0;top:0;width:1162px;height:136px;background:var(--page);border-bottom:2px solid #dcdcdc}
.soft-band{left:0;top:138px;width:1162px;height:477px;background:linear-gradient(#fbfbfb,#f6f6f6)}
.logo{left:97px;top:40px;font-family:"Gelasio",serif;font-weight:700;font-size:32px;color:var(--logo);letter-spacing:.3px}
.search{left:879px;top:32px;width:182px;height:40px;border:1px solid #999;border-radius:8px;background:var(--white);font-size:13px;color:#555;padding:11px 13px}
.search svg{position:absolute;right:4px;top:6px}
.nav{left:97px;top:119px;width:964px;height:46px;background:var(--nav)}
.nav a{position:absolute;top:11px;font-family:"PT Sans",sans-serif;font-weight:700;font-size:18px;color:var(--white);text-decoration:none;letter-spacing:1px}
.banner{left:97px;top:165px;width:964px;height:250px;box-shadow:0 12px 14px -8px rgba(0,0,0,.25)}
.strip{position:absolute;top:0;height:250px;display:flex;align-items:center;justify-content:center}
.strip span{transform:rotate(-90deg);white-space:nowrap;font-size:20px}
.strip-web{left:0;width:57px;background:var(--strip-light);color:#555}
.strip-agile{left:57px;width:63px;background:var(--strip-mid);color:var(--white)}
.banner-text{position:absolute;left:120px;top:0;width:438px;height:250px;background:var(--panel)}
.banner-text h1{font-family:"PT Sans",sans-serif;font-weight:700;font-size:17px;text-align:center;line-height:29px;margin-top:35px;letter-spacing:.6px}
.banner-text p{font-size:12px;line-height:29px;margin:6px 32px 0 32px;text-align:justify}
.banner-photo{position:absolute;left:558px;top:0;width:406px;height:250px;background:linear-gradient(120deg,#e9eae6,#b9b7b1 45%,#3a3a3a 70%,#d7d6d0)}
.team-photo{left:100px;top:449px;width:220px;height:163px;border-radius:8px;border:3px solid #e4e4e4;background:linear-gradient(135deg,#eeeeee,#8d8d8d 55%,#dedede);box-shadow:0 1px 3px rgba(0,0,0,.3)}
.welcome-title{left:360px;top:452px;font-size:30px;font-weight:400}
.welcome-text{left:360px;top:504px;width:703px;font-size:12.4px;line-height:29px;text-align:justify}
.intro{left:97px;top:631px;width:964px;font-size:12.4px;line-height:29px;color:var(--muted);text-align:justify}
.card{top:797px;width:286px;height:229px;border-radius:4px}
.card h2{font-weight:400;font-size:24px;padding:5px 0 0 30px;letter-spacing:.3px}
.card ul{position:absolute;left:13px;top:48px;width:259px;height:171px;background:var(--white);border-radius:12px;list-style:none;padding:16px 0 0 24px}
.card li{font-size:14.5px;height:35px;display:flex;align-items:center;gap:10px}
.card-projects{left:97px;background:var(--page);border:1px solid #aaa}
.card-projects h2{color:var(--dark)}
.card-services{left:435px;background:var(--mid)}
.card-services h2,.card-clients h2{color:var(--white)}
.card-clients{left:773px;background:var(--dark)}
.card-clients h2{padding-left:40px;padding-top:8px}
.footer{left:0;top:1082px;width:1162px;height:118px;background:var(--page)}
.partner{top:1118px;font-size:17px;color:var(--dark)}
.footer-links{left:0;top:1105px;width:1162px;text-align:center;font-size:14.5px;line-height:29px}
.footer-links a{color:var(--text);text-decoration:none}
.social{left:900px;top:1108px;width:161px;display:flex;justify-content:flex-end;gap:12px;font-size:14px;color:var(--dark);align-items:center;height:36px}
</style>
</head>
<body>
<div class="abs header-band"></div>
<div class="abs soft-band"></div>

<div class="abs logo">Sammalkivi</div>
<div class="abs search">Search
  <svg width="30" height="30" viewBox="0 0 30 30"><circle cx="12" cy="12" r="8" fill="none" stroke="#888" stroke-width="2"/><line x1="18" y1="18" x2="26" y2="26" stroke="#888" stroke-width="3" stroke-linecap="round"/></svg>
</div>

<nav class="abs nav">
  <a href="#" style="left:49px">Home</a>
  <a href="#" style="left:186px">About Us</a>
  <a href="#" style="left:337px">Projects</a>
  <a href="#" style="left:477px">Services</a>
  <a href="#" style="left:613px">Contact Us</a>
</nav>

<section class="abs banner">
  <div class="strip strip-web"><span>Web development</span></div>
  <div class="strip strip-agile"><span>Agile development</span></div>
  <div class="banner-text">
    <h1>Kahvi, Enterprise Kernel EE Application<br>Programming and Architectures</h1>
    <p>Lorem Ipsum is simply dummy text of the printing and typesetting industry. Lorem Ipsum has been the industry's standard dummy text ever since the 1500s</p>
  </div>
  <div class="banner-photo" role="img" aria-label="Photo of three consultants working together at a desk with papers and a laptop"></div>
</section>

<div class="abs team-photo" role="img" aria-label="Black and white photo of a business team seated around a meeting table"></div>
<h2 class="abs welcome-title">Welcome</h2>
<p class="abs welcome-text">Lorem Ipsum is simply dummy text of the printing and typesetting industry. Lorem Ipsum has been the industry's standard dummy text ever since the 1500s Lorem Ipsum is simply dummy text of the printing and typesetting industry. Lorem Ipsum has been the industry's standard dummy text ever since the 1500s, when an unknown printer took a galley of type and scrambled it to make a type specimen book. Maker including versions of Lorem Ipsum.</p>

<p class="abs intro">Lorem Ipsum is simply dummy text of the printing and typesetting industry. Lorem Ipsum has been the industry's standard dummy text ever since the 1500s, when an unknown printer took a galley of type and scrambled it to make a type specimen book. It has survived not only five centuries, but also the leap into electronic typesetting, remaining essentially unchanged. It was popularised in the 1960s with the release of Letraset sheets containing Lorem Ipsum passages, and more recently with desktop publishing software like Aldus PageMaker including versions of Lorem Ipsum.</p>

<svg width="0" height="0" style="position:absolute"><defs><symbol id="tick" viewBox="0 0 16 16"><path d="M1 9 L4 7 L7 11 L14 1 L15 2 L7 15 Z" fill="var(--tick)"/></symbol></defs></svg>

<section class="abs card card-projects">
  <h2>Our Projects</h2>
  <ul>
    <li><svg width="16" height="16"><use href="#tick"/></svg>Lorem Ipsum</li>
    <li><svg width="16" height="16"><use href="#tick"/></svg>Lorem Ipsum</li>
    <li><svg width="16" height="16"><use href="#tick"/></svg>Lorem Ipsum</li>
    <li><svg width="16" height="16"><use href="#tick"/></svg>Lorem Ipsum</li>
  </ul>
</section>
<section class="abs card card-services">
  <h2>Our Services</h2>
  <ul style="padding-left:36px;padding-top:20px">
    <li><svg width="16" height="16"><use href="#tick"/></svg>Lorem Ipsum</li>
    <li><svg width="16" height="16"><use href="#tick"/></svg>Lorem Ipsum</li>
    <li><svg width="16" height="16"><use href="#tick"/></svg>Lorem Ipsum</li>
    <li><svg width="16" height="16"><use href="#tick"/></svg>Lorem Ipsum</li>
  </ul>
</section>
<section class="abs card card-clients">
  <h2>Our Clients</h2>
  <ul style="left:16px;padding-left:34px;padding-top:19px">
    <li><svg width="16" height="16"><use href="#tick"/></svg>Lorem Ipsum</li>
    <li><svg width="16" height="16"><use href="#tick"/></svg>Lorem Ipsum</li>
    <li><svg width="16" height="16"><use href="#tick"/></svg>Lorem Ipsum</li>
    <li><svg width="16" height="16"><use href="#tick"/></svg>Lorem Ipsum</li>
  </ul>
</section>

<footer class="abs footer"></footer>
<div class="abs partner" style="left:118px">Kahvi</div>
<div class="abs partner" style="left:190px">Kernel EE</div>
<div class="abs footer-links">
  <a href="#">Home</a>&nbsp; | <a href="#">About Us</a> | <a href="#">Projects</a> | <a href="#">Services</a> | <a href="#">Contact Us</a><br>
  Copyright@2011 www.samsoco.fi
</div>
<div class="abs social"><span>Feed</span><span>Chirp</span><span>Friendly</span></div>
</body>
</html>
```